Bright Ledger Path's Mortgage Arc

For BrightLedgerPath.org - Creating a sequence of web pages for consumers to understand their mortgage through Mortgage Arc. There are six pages - want the designer to be willing to design and code those six pages. Most of the pages are very similar.

```html
<!DOCTYPE html>
<html lang="en">
<head>
<meta charset="utf-8">
<title>Bright Ledger Path – Mortgage Arc page variations</title>
<link href="https://fonts.googleapis.com/css2?family=Poppins:wght@400;500;600;700&display=swap" rel="stylesheet">
<style>
:root{
  --sheet:#4a4a4a;
  --page:#eaeffb;
  --brand-blue:#1a4fd0;
  --deep-blue:#1955c9;
  --brand-green:#0aa85a;
  --mint:#d6fbe7;
  --bright-green:#22d28e;
  --card:#ffffff;
  --ink:#1d1d1f;
  --muted:#4d4f57;
  --accent:#17c27e;
  --label-white:#ffffff;
}
*{box-sizing:border-box;margin:0;padding:0}
html,body{width:1066px;height:1200px;overflow:hidden;background:var(--sheet);font-family:"Poppins",sans-serif}
.sheet{position:relative;width:1066px;height:1200px}
.sample-label{position:absolute;color:#fff;font-size:21px;font-weight:400;transform:translate(-50%,-50%);white-space:nowrap;letter-spacing:.3px}

.board{position:absolute;width:670px;height:490px;background:var(--page);transform-origin:0 0;transform:scale(.587)}
.board__title{position:absolute;left:0;right:0;top:40px;text-align:center;color:var(--brand-blue);font-size:24px;font-weight:700}
.board__footer{position:absolute;left:0;right:0;top:436px;text-align:center;color:var(--muted);font-size:8px}
.board__footer span{margin:0 5px}

.tile{position:absolute;background:var(--card);border-radius:7px;box-shadow:0 2px 8px rgba(30,50,110,.08);text-align:center;color:var(--icon-main,var(--brand-blue))}
.tile svg{display:block;margin:0 auto}
.tile__label{color:var(--muted);font-weight:500;line-height:1.35}
.tile--solo{width:106px;height:96px}
.tile--solo svg{width:42px;height:42px;margin-top:14px}
.tile--solo .tile__label{font-size:7.6px;margin-top:6px}
.tile--qualify{left:282px;top:90px}
.tile--profile{left:283px;top:313px}
.tile--mini{width:82px;height:76px}
.tile--mini svg{width:32px;height:32px;margin-top:10px}
.tile--mini .tile__label{font-size:5.8px;margin-top:4px}
.tile--top{left:65px;top:49px}
.group--wide-top .tile--top{left:20px;width:171px}
.tile--bl{left:20px;top:131px}
.tile--br{left:109px;top:131px}

.group{position:absolute;top:135px;width:213px;height:223px;border-radius:8px;color:var(--ink)}
.group--left{left:55px}
.group--right{left:401px}
.group__tag{position:absolute;top:-10px;left:50%;transform:translateX(-50%);height:19px;padding:0 7px;border-radius:4px;background:var(--brand-blue);color:#fff;font-size:8.4px;font-weight:600;line-height:19px;white-space:nowrap}
.group__tag--green{background:var(--brand-green)}
.group__lead{position:absolute;top:20px;left:0;right:0;text-align:center;font-size:5.6px}
.group__amount{position:absolute;top:30px;left:0;right:0;text-align:center;font-size:8.6px;font-weight:700}

.group--mint{background:var(--mint)}
.group--white{background:var(--card);box-shadow:0 2px 8px rgba(30,50,110,.06)}
.group--gradient{background:linear-gradient(180deg,var(--deep-blue) 0%,var(--brand-green) 100%);color:#fff}
.group--green{background:var(--brand-green);color:#fff}
.group--blue{background:var(--deep-blue);color:#fff}
.group--bright{background:var(--bright-green);color:#fff}
.group--bright .tile{background:var(--deep-blue);--icon-main:#bff5dc}
.group--bright .tile__label{color:var(--label-white)}

.ac{stroke:var(--accent)}
</style>
</head>
<body>
<svg width="0" height="0" style="position:absolute" aria-hidden="true">
  <defs>
    <symbol id="icon-house-cash" viewBox="0 0 40 40" fill="none" stroke="currentColor" stroke-width="1.5" stroke-linejoin="round">
      <path d="M14 16 L24 7 L34 16 M17 14 V24 M31 14 V28"/>
      <rect x="22" y="12" width="4" height="4"/>
      <rect x="5" y="21" width="22" height="12" rx="1" class="ac"/>
      <circle cx="16" cy="27" r="4" class="ac"/>
      <path d="M16 25 V29" class="ac"/>
    </symbol>
    <symbol id="icon-house-coin" viewBox="0 0 40 40" fill="none" stroke="currentColor" stroke-width="1.5" stroke-linejoin="round">
      <path d="M5 18 L18 7 L31 18 M8 16 V33 H24 M28 16 V22"/>
      <rect x="13" y="20" width="6" height="6"/>
      <circle cx="29" cy="29" r="6" class="ac"/>
      <path d="M29 26 V32" class="ac"/>
    </symbol>
    <symbol id="icon-hand-house" viewBox="0 0 40 40" fill="none" stroke="currentColor" stroke-width="1.5" stroke-linejoin="round">
      <path d="M11 13 L19 6 L27 13 M13 12 V22 H25 V12"/>
      <circle cx="21" cy="18" r="4" class="ac"/>
      <path d="M4 28 H12 L20 31 H30 L36 26 M12 34 L20 36 H30"/>
    </symbol>
    <symbol id="icon-bars-arrow" viewBox="0 0 40 40" fill="none" stroke="currentColor" stroke-width="1.5" stroke-linejoin="round">
      <path d="M5 35 H35 M9 35 V20 H14 V35 M18 35 V24 H23 V35 M27 35 V29 H32 V35"/>
      <path d="M12 8 L20 14 L26 10 L32 18 M28 18 H32 V14" class="ac"/>
    </symbol>
    <symbol id="icon-bars-house" viewBox="0 0 40 40" fill="none" stroke="currentColor" stroke-width="1.5" stroke-linejoin="round">
      <path d="M3 34 H37 M5 34 V18 H9 V34 M12 34 V22 H16 V34 M19 34 V26 H23 V34"/>
      <path d="M24 27 L30 21 L37 27 M26 26 V34 M35 26 V34"/>
      <circle cx="20" cy="10" r="5" class="ac"/>
      <path d="M20 8 V12" class="ac"/>
    </symbol>
    <symbol id="icon-bars-coin" viewBox="0 0 40 40" fill="none" stroke="currentColor" stroke-width="1.5" stroke-linejoin="round">
      <path d="M4 34 H36 M6 34 V14 H10 V34 M14 34 V20 H18 V34 M22 34 V25 H26 V34 M30 34 V29 H34 V34"/>
      <circle cx="28" cy="10" r="6" class="ac"/>
      <path d="M28 7 V13" class="ac"/>
    </symbol>
    <symbol id="icon-docs" viewBox="0 0 40 40" fill="none" stroke="currentColor" stroke-width="1.5" stroke-linejoin="round">
      <rect x="15" y="4" width="18" height="24" rx="1" transform="rotate(8 24 16)"/>
      <rect x="10" y="8" width="18" height="24" rx="1"/>
      <path d="M14 14 H24 M14 18 H24 M14 22 H19"/>
      <circle cx="23" cy="25" r="4" class="ac"/>
      <rect x="4" y="26" width="9" height="10" rx="2"/>
    </symbol>
    <symbol id="icon-profile-edit" viewBox="0 0 40 40" fill="none" stroke="currentColor" stroke-width="1.5" stroke-linejoin="round">
      <rect x="6" y="4" width="22" height="32" rx="1"/>
      <circle cx="17" cy="13" r="5" class="ac"/>
      <path d="M10 24 H22 M10 28 H22 M10 32 H18"/>
      <path d="M34 12 L37 15 L26 30 L22 32 L23 27 Z" class="ac"/>
    </symbol>
  </defs>
</svg>

<main class="sheet">
  <p class="sample-label" style="left:293px;top:66px">Sample 1</p>
  <p class="sample-label" style="left:774px;top:65px">Sample 2</p>
  <p class="sample-label" style="left:284px;top:437px">Sample 3</p>
  <p class="sample-label" style="left:764px;top:436px">Sample 4</p>
  <p class="sample-label" style="left:561px;top:816px">Sample 5</p>

  <!-- variation 1 -->
  <section class="board" style="left:108.6px;top:113.3px">
    <h1 class="board__title">Mortgage Central</h1>
    <div class="group group--left group--mint">
      <span class="group__tag">Specific Payment</span>
      <p class="group__lead">Increase Your Purchasung Power by Up to</p>
      <p class="group__amount">$ 25, 000</p>
      <div class="tile tile--mini tile--top"><svg><use href="#icon-house-cash"/></svg><p class="tile__label">Your Specific<br>Mortgage Payment</p></div>
      <div class="tile tile--mini tile--bl"><svg><use href="#icon-hand-house"/></svg><p class="tile__label">Purchasing Power<br>by Mortgage</p></div>
      <div class="tile tile--mini tile--br"><svg><use href="#icon-bars-arrow"/></svg><p class="tile__label">Improve Your<br>Purchasing Power</p></div>
    </div>
    <div class="tile tile--solo tile--qualify"><svg><use href="#icon-docs"/></svg><p class="tile__label">Maximum Mortgage<br>Qualifications</p></div>
    <div class="tile tile--solo tile--profile"><svg><use href="#icon-profile-edit"/></svg><p class="tile__label">Edit Your<br>Mortgage Profile</p></div>
    <div class="group group--right group--mint">
      <span class="group__tag">Specific Property</span>
      <p class="group__lead">Lower Your Monthly Payment by as Much as</p>
      <p class="group__amount">$ 250</p>
      <div class="tile tile--mini tile--top"><svg><use href="#icon-house-coin"/></svg><p class="tile__label">Your Specific<br>Mortgage Amount</p></div>
      <div class="tile tile--mini tile--bl"><svg><use href="#icon-bars-house"/></svg><p class="tile__label">Payment Reduction<br>by Mortgage</p></div>
      <div class="tile tile--mini tile--br"><svg><use href="#icon-bars-coin"/></svg><p class="tile__label">Your Payment<br>Reduction Payment</p></div>
    </div>
    <p class="board__footer">Copyright 2023 by Bright Ledger Path. Terms Of Use<span>|</span>Privacy Statement</p>
  </section>

  <!-- variation 2 -->
  <section class="board" style="left:564.7px;top:113.3px">
    <h1 class="board__title">Mortgage Central</h1>
    <div class="group group--left group--white group--wide-top">
      <span class="group__tag">Specific Payment</span>
      <p class="group__lead">Increase Your Purchasung Power by Up to</p>
      <p class="group__amount">$ 25, 000</p>
      <div class="tile tile--mini tile--top"><svg><use href="#icon-house-cash"/></svg><p class="tile__label">Your Specific<br>Mortgage Payment</p></div>
      <div class="tile tile--mini tile--bl"><svg><use href="#icon-hand-house"/></svg><p class="tile__label">Purchasing Power<br>by Mortgage</p></div>
      <div class="tile tile--mini tile--br"><svg><use href="#icon-bars-arrow"/></svg><p class="tile__label">Improve Your<br>Purchasing Power</p></div>
    </div>
    <div class="tile tile--solo tile--qualify"><svg><use href="#icon-docs"/></svg><p class="tile__label">Maximum Mortgage<br>Qualifications</p></div>
    <div class="tile tile--solo tile--profile"><svg><use href="#icon-profile-edit"/></svg><p class="tile__label">Edit Your<br>Mortgage Profile</p></div>
    <div class="group group--right group--white group--wide-top">
      <span class="group__tag group__tag--green">Specific Property</span>
      <p class="group__lead">Lower Your Monthly Payment by as Much as</p>
      <p class="group__amount">$ 250</p>
      <div class="tile tile--mini tile--top"><svg><use href="#icon-house-coin"/></svg><p class="tile__label">Your Specific<br>Mortgage Amount</p></div>
      <div class="tile tile--mini tile--bl"><svg><use href="#icon-bars-house"/></svg><p class="tile__label">Payment Reduction<br>by Mortgage</p></div>
      <div class="tile tile--mini tile--br"><svg><use href="#icon-bars-coin"/></svg><p class="tile__label">Your Payment<br>Reduction Payment</p></div>
    </div>
    <p class="board__footer">Copyright 2023 by Bright Ledger Path. Terms Of Use<span>|</span>Privacy Statement</p>
  </section>

  <!-- variation 3 -->
  <section class="board" style="left:109.8px;top:479px">
    <h1 class="board__title">Mortgage Central</h1>
    <div class="group group--left group--gradient">
      <span class="group__tag group__tag--green">Specific Payment</span>
      <p class="group__lead">Increase Your Purchasung Power by Up to</p>
      <p class="group__amount">$ 25, 000</p>
      <div class="tile tile--mini tile--top"><svg><use href="#icon-house-cash"/></svg><p class="tile__label">Your Specific<br>Mortgage Payment</p></div>
      <div class="tile tile--mini tile--bl"><svg><use href="#icon-hand-house"/></svg><p class="tile__label">Purchasing Power<br>by Mortgage</p></div>
      <div class="tile tile--mini tile--br"><svg><use href="#icon-bars-arrow"/></svg><p class="tile__label">Improve Your<br>Purchasing Power</p></div>
    </div>
    <div class="tile tile--solo tile--qualify"><svg><use href="#icon-docs"/></svg><p class="tile__label">Maximum Mortgage<br>Qualifications</p></div>
    <div class="tile tile--solo tile--profile"><svg><use href="#icon-profile-edit"/></svg><p class="tile__label">Edit Your<br>Mortgage Profile</p></div>
    <div class="group group--right group--gradient">
      <span class="group__tag group__tag--green">Specific Property</span>
      <p class="group__lead">Lower Your Monthly Payment by as Much as</p>
      <p class="group__amount">$ 250</p>
      <div class="tile tile--mini tile--top"><svg><use href="#icon-house-coin"/></svg><p class="tile__label">Your Specific<br>Mortgage Amount</p></div>
      <div class="tile tile--mini tile--bl"><svg><use href="#icon-bars-house"/></svg><p class="tile__label">Payment Reduction<br>by Mortgage</p></div>
      <div class="tile tile--mini tile--br"><svg><use href="#icon-bars-coin"/></svg><p class="tile__label">Your Payment<br>Reduction Payment</p></div>
    </div>
    <p class="board__footer">Copyright 2023 by Bright Ledger Path. Terms Of Use<span>|</span>Privacy Statement</p>
  </section>

  <!-- variation 4 -->
  <section class="board" style="left:564.7px;top:479px">
    <h1 class="board__title">Mortgage Central</h1>
    <div class="group group--left group--green group--wide-top">
      <span class="group__tag">Specific Payment</span>
      <p class="group__lead">Increase Your Purchasung Power by Up to</p>
      <p class="group__amount">$ 25, 000</p>
      <div class="tile tile--mini tile--top"><svg><use href="#icon-house-cash"/></svg><p class="tile__label">Your Specific<br>Mortgage Payment</p></div>
      <div class="tile tile--mini tile--bl"><svg><use href="#icon-hand-house"/></svg><p class="tile__label">Purchasing Power<br>by Mortgage</p></div>
      <div class="tile tile--mini tile--br"><svg><use href="#icon-bars-arrow"/></svg><p class="tile__label">Improve Your<br>Purchasing Power</p></div>
    </div>
    <div class="tile tile--solo tile--qualify"><svg><use href="#icon-docs"/></svg><p class="tile__label">Maximum Mortgage<br>Qualifications</p></div>
    <div class="tile tile--solo tile--profile"><svg><use href="#icon-profile-edit"/></svg><p class="tile__label">Edit Your<br>Mortgage Profile</p></div>
    <div class="group group--right group--blue group--wide-top">
      <span class="group__tag group__tag--green">Specific Property</span>
      <p class="group__lead">Lower Your Monthly Payment by as Much as</p>
      <p class="group__amount">$ 250</p>
      <div class="tile tile--mini tile--top"><svg><use href="#icon-house-coin"/></svg><p class="tile__label">Your Specific<br>Mortgage Amount</p></div>
      <div class="tile tile--mini tile--bl"><svg><use href="#icon-bars-house"/></svg><p class="tile__label">Payment Reduction<br>by Mortgage</p></div>
      <div class="tile tile--mini tile--br"><svg><use href="#icon-bars-coin"/></svg><p class="tile__label">Your Payment<br>Reduction Payment</p></div>
    </div>
    <p class="board__footer">Copyright 2023 by Bright Ledger Path. Terms Of Use<span>|</span>Privacy Statement</p>
  </section>

  <!-- variation 5 -->
  <section class="board" style="left:364.5px;top:864px">
    <h1 class="board__title">Mortgage Central</h1>
    <div class="group group--left group--bright">
      <span class="group__tag">Specific Payment</span>
      <p class="group__lead">Increase Your Purchasung Power by Up to</p>
      <p class="group__amount">$ 25, 000</p>
      <div class="tile tile--mini tile--top"><svg><use href="#icon-house-cash"/></svg><p class="tile__label">Your Specific<br>Mortgage Payment</p></div>
      <div class="tile tile--mini tile--bl"><svg><use href="#icon-hand-house"/></svg><p class="tile__label">Purchasing Power<br>by Mortgage</p></div>
      <div class="tile tile--mini tile--br"><svg><use href="#icon-bars-arrow"/></svg><p class="tile__label">Improve Your<br>Purchasing Power</p></div>
    </div>
    <div class="tile tile--solo tile--qualify"><svg><use href="#icon-docs"/></svg><p class="tile__label">Maximum Mortgage<br>Qualifications</p></div>
    <div class="tile tile--solo tile--profile"><svg><use href="#icon-profile-edit"/></svg><p class="tile__label">Edit Your<br>Mortgage Profile</p></div>
    <div class="group group--right group--bright">
      <span class="group__tag">Specific Property</span>
      <p class="group__lead">Lower Your Monthly Payment by as Much as</p>
      <p class="group__amount">$ 250</p>
      <div class="tile tile--mini tile--top"><svg><use href="#icon-house-coin"/></svg><p class="tile__label">Your Specific<br>Mortgage Amount</p></div>
      <div class="tile tile--mini tile--bl"><svg><use href="#icon-bars-house"/></svg><p class="tile__label">Payment Reduction<br>by Mortgage</p></div>
      <div class="tile tile--mini tile--br"><svg><use href="#icon-bars-coin"/></svg><p class="tile__label">Your Payment<br>Reduction Payment</p></div>
    </div>
    <p class="board__footer">Copyright 2023 by Bright Ledger Path. Terms Of Use<span>|</span>Privacy Statement</p>
  </section>
</main>
</body>
</html>
```